RO Interiors Website Re-Design

I am an interior designer. What I do, is work with customers to design spaces in their homes prior to a contractor doing the work. This could be kitchens, bathrooms, offices, and more. I have uploaded a file, and it has my URL within it for you to use as a reference.
https://rointeriors-studio.example/

Industry/Entity Type

Interior Design

Coding

Coded - Design and coding required

Number of Pages Required

5+ page

Requirements
Must have
• Clean, professional, easy to navigate, color schemes should follow what is on my current site, also written content you can pull from my current site as well along with the current script / font

```html
<!DOCTYPE html>
<html lang="en">
<head>
<meta charset="UTF-8">
<title>RO Interiors</title>
<link rel="stylesheet" href="https://fonts.googleapis.com/css2?family=Inter:wght@400;500;600;700;800&display=swap">
<style>
:root{
  --gold:#d9a12a;
  --orange:#f29a1c;
  --ink:#1c2230;
  --text:#3a3f4a;
  --muted:#6b7080;
  --navy:#0b1a3d;
  --foot-text:rgba(255,255,255,.82);
  --card:#fbfbfc;
  --link-icon:#8b5cf6;
  --white:#ffffff;
}
*{box-sizing:border-box;margin:0;padding:0}
html,body{width:1200px;height:2355px;overflow:hidden}
body{font-family:'Inter',sans-serif;color:var(--text);background:var(--white);position:relative}
.abs{position:absolute}

/* header */
.brand{left:75px;top:26px;font-size:28px;font-weight:500;color:var(--ink);letter-spacing:.5px}
.nav{left:432px;top:36px;display:flex;gap:27px;font-size:14px;color:var(--text)}
.nav a{color:inherit;text-decoration:none}
.nav .active{color:var(--gold)}
.btn-contact{left:996px;top:22px;width:129px;height:43px;border:1.5px solid var(--gold);border-radius:3px;color:var(--gold);font-size:14px;font-weight:600;display:flex;align-items:center;justify-content:center}

/* hero */
.hero-title{left:173px;top:178px;font-size:45px;font-weight:800;line-height:51px;color:var(--ink);letter-spacing:-.5px}
.hero-title .accent{color:var(--gold);border-bottom:3px solid var(--gold)}
.hero-sub{left:173px;top:352px;font-size:15px;font-weight:500;color:var(--ink)}
.hero-copy{left:173px;top:383px;width:430px;font-size:15px;line-height:24px;color:var(--muted)}
.features{left:173px;top:478px;display:grid;grid-template-columns:227px 227px;row-gap:18px;font-size:15px;font-weight:500;color:var(--ink)}
.features li{list-style:none;display:flex;align-items:center;gap:6px;height:21px}
.hero-back{left:839px;top:150px;width:286px;height:324px;border-radius:0 150px 0 0;background:linear-gradient(160deg,#1f2a44,#3b4a6a 50%,#c9ccd2);z-index:2}
.hero-front{left:663px;top:260px;width:296px;height:248px;border-radius:60px 0 110px 4px;background:linear-gradient(135deg,#2d4472,#8a8f99 50%,#e5e2dc)}

/* experience */
.exp-title{left:0;width:1200px;top:668px;text-align:center;font-size:30px;font-weight:700;color:var(--ink)}
.exp-title span{color:var(--orange);border-bottom:2px solid var(--orange)}
.exp-copy{left:280px;width:640px;top:721px;text-align:center;font-size:13.5px;line-height:22px;color:var(--muted)}
.exp-photo{left:318px;top:831px;width:564px;height:281px;border-radius:14px;background:linear-gradient(120deg,#3a4356,#6b6458 50%,#a88a66)}

.cards{left:173px;top:1157px;display:flex;gap:18px}
.card{width:273px;height:337px;background:var(--card);border-radius:4px;box-shadow:0 2px 8px rgba(0,0,0,.06);overflow:hidden}
.card-photo{height:191px}
.card-body{padding:23px 22px}
.card h3{font-size:18px;font-weight:500;color:var(--ink);line-height:25px;margin-bottom:9px}
.card p{font-size:13.5px;line-height:22px;color:var(--muted)}

/* founder */
.founder{left:0;top:1564px;width:1200px;height:361px;background:linear-gradient(90deg,#5a4a32,#3f5a38 40%,#4a6a3e 70%,#7a6a4a)}
.founder-photo{left:245px;top:1564px;width:336px;height:361px;background:linear-gradient(180deg,#4a3a2e,#7a6a5c 55%,#2b2522)}
.founder-name{left:619px;top:1620px;font-size:29px;color:var(--white);font-weight:500}
.founder-role{left:635px;top:1662px;font-size:13.5px;line-height:22px;font-weight:700;color:var(--white)}
.role-mark{left:617px;top:1662px}
.founder-bio{left:619px;top:1722px;width:335px;font-size:13.5px;line-height:22px;color:rgba(255,255,255,.78)}

/* footer */
.footer-band{left:0;top:1925px;width:1200px;height:430px;background:var(--navy)}
.foot-brand{left:175px;top:2003px;font-size:29px;font-weight:700;color:var(--white)}
.foot-about{left:175px;top:2054px;font-size:12px;line-height:19.5px;color:var(--foot-text)}
.foot-contact{left:175px;top:2110px;font-size:12.5px;line-height:25px;color:var(--foot-text)}
.foot-contact div{display:flex;align-items:center;gap:9px}
.foot-h{font-size:15px;font-weight:500;color:var(--white)}
.foot-menu{left:492px;top:2008px}
.foot-menu ul{margin-top:21px;list-style:none;font-size:12px;line-height:27px;color:var(--foot-text)}
.foot-open{left:647px;top:2008px}
.foot-open p{margin-top:21px;font-size:12px;line-height:19.5px;color:var(--foot-text)}
.foot-social{left:880px;top:2008px}
.socials{margin-top:24px;display:flex;gap:30px}
.socials span{width:23px;height:23px;border-radius:50%;background:rgba(255,255,255,.85);display:block}
.foot-rule{left:171px;top:2292px;width:858px;height:1px;background:rgba(255,255,255,.3)}
.copyright{left:0;width:1200px;top:2318px;text-align:center;font-size:10px;color:var(--foot-text)}
</style>
</head>
<body>

<header>
  <div class="abs brand">RO Interiors</div>
  <nav class="abs nav">
    <a class="active" href="#">Home</a><a href="#">Portfolio</a><a href="#" style="color:var(--ink)">Services</a><a href="#">FAQs</a><a href="#">Contact</a>
  </nav>
  <a class="abs btn-contact">Contact</a>
</header>

<section>
  <h1 class="abs hero-title">Your choice is our<br>first and foremost<br><span class="accent">Priority</span></h1>
  <p class="abs hero-sub">The Real Creative Potential</p>
  <p class="abs hero-copy">We make spaces and structures for our customers and local area itedes malis civibus kase iuvaret blandit ipsum Past more emotionless this.</p>
  <ul class="abs features">
    <li><svg width="15" height="15" viewBox="0 0 24 24" fill="none" stroke="var(--link-icon)" stroke-width="2"><path d="M9 8H7a4 4 0 000 8h2M15 8h2a4 4 0 010 8h-2M8 12h8"/></svg>Home Remodelling</li>
    <li><svg width="15" height="15" viewBox="0 0 24 24" fill="none" stroke="var(--link-icon)" stroke-width="2"><path d="M9 8H7a4 4 0 000 8h2M15 8h2a4 4 0 010 8h-2M8 12h8"/></svg>the Modern Approach</li>
    <li><svg width="15" height="15" viewBox="0 0 24 24" fill="none" stroke="var(--link-icon)" stroke-width="2"><path d="M9 8H7a4 4 0 000 8h2M15 8h2a4 4 0 010 8h-2M8 12h8"/></svg>Exceptional Service</li>
    <li><svg width="15" height="15" viewBox="0 0 24 24" fill="none" stroke="var(--link-icon)" stroke-width="2"><path d="M9 8H7a4 4 0 000 8h2M15 8h2a4 4 0 010 8h-2M8 12h8"/></svg>Design Development</li>
  </ul>
  <div class="abs hero-front" role="img" aria-label="Bedroom with navy wall, birch tree artwork and white bedding"></div>
  <div class="abs hero-back" role="img" aria-label="Pendant globe lights in front of an arched window on a navy wall"></div>
</section>

<section>
  <h2 class="abs exp-title">25+ Years of <span>Experience</span></h2>
  <p class="abs exp-copy">2 Past more emotionless this along goodness this sad wow manatee mongos flustered noteworthy man comedian opened inside owing correctionally around after inefficient telling spransac briskly speckles customer. Squid reluctantly gibbered.</p>
  <div class="abs exp-photo" role="img" aria-label="Home bar with wooden counter, shelves of bottles and wall-mounted TV"></div>

  <div class="abs cards">
    <article class="card">
      <div class="card-photo" role="img" aria-label="Bathroom vanity with wood plank wall and dark mirror" style="background:linear-gradient(135deg,#2a2a30,#6a5a4c 50%,#c8c4be)"></div>
      <div class="card-body"><h3>Residential Design</h3><p>2 Past more emotionless this along goodness this sad wow manatee mongos</p></div>
    </article>
    <article class="card">
      <div class="card-photo" role="img" aria-label="Cream upholstered armchair with wooden frame" style="background:linear-gradient(135deg,#d8d2c8,#8a6a4a 55%,#efece6)"></div>
      <div class="card-body"><h3>Home Renovations and Remodels</h3><p>2 Past more emotionless this along goodness this sad wow manatee</p></div>
    </article>
    <article class="card">
      <div class="card-photo" role="img" aria-label="Brown leather armchair beside a window with a wall lamp" style="background:linear-gradient(135deg,#a8b0a8,#8a5a3a 55%,#dcdcd8)"></div>
      <div class="card-body"><h3>Furnish and Style</h3><p>2 Past more emotionless this along goodness this sad wow manatee mongos</p></div>
    </article>
  </div>
</section>

<section>
  <div class="abs founder" role="img" aria-label="Softly blurred interior with plants and a pink chair"></div>
  <div class="abs founder-photo" role="img" aria-label="Portrait of the lead designer standing in her office"></div>
  <h2 class="abs founder-name">Maren Holloway</h2>
  <svg class="abs role-mark" width="12" height="46" viewBox="0 0 12 46"><line x1="6" y1="0" x2="6" y2="36" stroke="#e6f23a" stroke-width="2" stroke-dasharray="4 3"/><circle cx="6" cy="40" r="5.5" fill="#e6f23a"/></svg>
  <p class="abs founder-role">Principle Lead Designer<br>and RO Interiors Founder</p>
  <p class="abs founder-bio">Maren is known for her passion in creating elegant and inviting spaces. She delivers creative elements, inspiration, and quality designs to a broad range of residential interiors, luxury apartments, and vacation homes. She strives to keep interiors comfortable &amp; functional while introducing the classic trends in design.</p>
</section>

<footer>
  <div class="abs footer-band"></div>
  <div class="abs foot-brand">Ro Interiors</div>
  <p class="abs foot-about">Serving the Cedar Valley and<br>surrounding areasCedar Valley, ST</p>
  <div class="abs foot-contact">
    <div><svg width="14" height="14" viewBox="0 0 24 24" fill="#3bb54a"><path d="M6.6 10.8a15 15 0 006.6 6.6l2.2-2.2a1 1 0 011-.25 11.4 11.4 0 003.6.57 1 1 0 011 1V20a1 1 0 01-1 1A17 17 0 013 4a1 1 0 011-1h3.5a1 1 0 011 1c0 1.25.2 2.45.57 3.57a1 1 0 01-.25 1z"/></svg>(555) 014-2290</div>
    <div><svg width="14" height="14" viewBox="0 0 24 24" fill="none" stroke="var(--gold)" stroke-width="2"><rect x="3" y="5" width="18" height="14" rx="1"/><path d="M3 6l9 7 9-7"/></svg>hello@rointeriors-studio.example</div>
  </div>
  <div class="abs foot-menu"><div class="foot-h">Menu</div><ul><li>Home</li><li>Portfolio</li><li>Services</li><li>FAQs</li><li>Contact</li></ul></div>
  <div class="abs foot-open"><div class="foot-h">Openings</div><p>Mon-Fri | 9am-5pm<br>Sat &amp; Sun | Closed</p></div>
  <div class="abs foot-social"><div class="foot-h">Connect Online</div><div class="socials"><span></span><span></span><span></span></div></div>
  <div class="abs foot-rule"></div>
  <p class="abs copyright">Copyright 2023 Ro Interiors. All Rights Reserved.</p>
</footer>

</body>
</html>
```